AMBER HARBOUR WEB

We need a home design in wordpress, we have now a web but we would like to improve it. Our current web is www.amberharbourvillas.example Our business is holliday rental of villas in Ibiza. Our guest must know that we are a reliable company, professional and with experience and good reviews. We want them to click in our reservation engine: https://bookings.amberharbourvillas.example/en/ and make reservation in our website. We would also like to say that all the properties that we have are just us who commercialize so we have best price available. Many people are going to see our villas in staylodgr.example and look to our website to make a reservation with us so we need to show them that they are at the right place and click at our link to our reservation engine. What make us special is that we are a local company, we are from Ibiza, Our guests are always received in person by the Amber Harbour Villas team. You will enjoy extensive tourist information when you check in and during the entire stay. You will be attended by ChatPelt and calls, always happy to help so that you have a happy and fun stay! Our guest stay is better than in hotel as they have more spece, private swiming pool, private garden, barbeque ... To rent a villa is the best way to stay in Ibiza. We also have a promotional video: https://vidshare.example/Qm7pTz3RxLa Let our philosophy be shown, we think that coming on holiday to Ibiza implies seeing the nature that we have in Ibiza, hence our name AMBER HARBOUR, like the pins that almost touch the sea in Ibiza, or the posidonea meadows where the intense green of the seaweed and the blue of the sea. We are aware of the environment, and we love Ibiza. For us, the client who visits Ibiza, should rent a car, go around the island, eat in a restaurant one day in front of the sea, is a night of partying to the discs, go shopping, visit the ancient heritage of Umanity, make some aquatic sport, enjoy the pool, those are for us Ibiza.

Target Market(s)

Europe, people from Holand, UK, Germany, France, Spain ...

Industry/Entity Type

Tourism

Colors

Designer to choose colors to be used in the design.

Requirements
Must have
• Pictures of Ibiza.
Nice to have
• Our name Amber Harbour Villas is beacuse in Ibiza there is forest that almost touch the watter of the Mediterranean sea, so you can see green of the forest and blue of the sea and the sky. And also beacause under the watter of the sea there is a plant called Posidonia that is also green please see the picture of posidonia.

```html
<!DOCTYPE html>
<html lang="en">
<head>
<meta charset="utf-8">
<title>Amber Harbour Villas Ibiza</title>
<link rel="stylesheet" href="https://fonts.googleapis.com/css2?family=Raleway:wght@400;500;600;700&family=Playfair+Display:wght@400&display=swap">
<style>
:root{
  --green:#9cbd3a;
  --green-dark:#7fa12a;
  --navy:#0d4668;
  --navy-deep:#0a3552;
  --ink:#333;
  --muted:#666;
  --title-blue:#2f3a8f;
  --price-red:#e04a4f;
  --pink:#e8437c;
  --line:#e4e4e4;
  --page:#f4f6f8;
  --footer:#1b1b1b;
  --footer-bottom:#111;
  --serif:'Playfair Display', Georgia, serif;
  --sans:'Raleway', Arial, sans-serif;
}
*{box-sizing:border-box;margin:0;padding:0}
html,body{width:1200px;height:3243px;overflow:hidden}
body{font-family:var(--sans);color:var(--ink);background:#fff;position:relative}
.abs{position:absolute}

/* header */
.site-header{position:absolute;left:0;top:0;width:1200px;height:122px;background:#fff}
.brand{position:absolute;left:172px;top:36px;display:flex;align-items:center;gap:12px}
.brand-dot{width:40px;height:40px;border-radius:50%;background:var(--green)}
.brand-name{font-family:var(--sans);font-weight:700;font-size:30px;color:var(--green-dark);letter-spacing:1px}
.search-box{position:absolute;left:566px;top:60px;width:148px;height:38px;border:1px solid #d6d6d6;border-radius:20px;font-size:13px;color:#999;padding:10px 16px}
.header-tools{position:absolute;right:168px;top:68px;display:flex;align-items:center;gap:14px;font-size:13px;color:var(--muted)}
.flag{width:16px;height:11px;background:#c8102e}
.header-tools .login{color:var(--navy);font-weight:600}
.header-tools .sep{width:1px;height:18px;background:#ccc}

/* nav */
.main-nav{position:absolute;left:0;top:122px;width:1200px;height:46px;background:var(--navy)}
.main-nav ul{position:absolute;left:170px;top:15px;display:flex;gap:26px;list-style:none}
.main-nav li{font-size:12px;font-weight:700;color:#fff;letter-spacing:.3px}
.main-nav li.active{color:var(--green)}
.follow{position:absolute;right:170px;top:11px;display:flex;align-items:center;gap:8px;color:#fff;font-size:12px}
.follow span.c{width:22px;height:22px;border-radius:50%;background:#2a8fd0}
.follow span.c.red{background:#d6453c}

/* hero */
.hero{position:absolute;left:0;top:168px;width:1200px;height:454px;background:linear-gradient(180deg,#3f88c9 0%,#7fb5df 28%,#2a7fa8 50%,#35a0b8 62%,#d9c9a8 78%,#c8b48c 100%)}
.hero-copy{position:absolute;left:170px;top:96px;width:460px;color:#fff}
.tag{display:inline-block;background:rgba(30,30,30,.75);color:#fff;font-size:12px;font-weight:700;padding:5px 12px}
.hero h1{font-size:28px;font-weight:700;margin-top:14px;letter-spacing:.3px}
.hero h2{font-size:26px;font-weight:500;margin-top:8px}
.hero p{font-size:13px;font-weight:600;line-height:19px;margin-top:18px}
.btn{display:inline-block;background:var(--green);color:#fff;font-size:12px;font-weight:700;text-align:center;letter-spacing:.4px}
.hero .btn{margin-top:20px;width:136px;height:40px;line-height:40px}
.slide-arrow{position:absolute;top:198px;width:26px;height:44px;background:rgba(20,20,20,.75)}
.slide-arrow svg{position:absolute;left:8px;top:15px}

/* intro */
.intro{position:absolute;left:0;top:622px;width:1200px;height:1400px;background:var(--page)}
.intro h2{position:absolute;top:74px;width:1200px;text-align:center;font-size:25px;font-weight:700;color:#222}
.intro .sub{position:absolute;top:124px;width:1200px;text-align:center;font-size:12px;font-weight:600;color:#333}
.search-bar{position:absolute;left:168px;top:202px;width:854px;height:43px;background:#fff;border:1px solid var(--line);display:flex;padding:6px;gap:6px}
.search-bar .field{flex:1;border:1px solid var(--line);font-size:12px;color:#777;padding:8px 10px;position:relative}
.search-bar .field svg{position:absolute;right:8px;top:10px}
.results{position:absolute;left:170px;top:266px;width:852px;display:flex;align-items:center;font-size:12px;color:#333}
.results .count{flex:1}
.results .clear{margin-right:14px}
.results .f-btn{background:#5f7d2c;color:#fff;padding:8px 14px;font-weight:700;margin-right:10px}
.results .m-btn{background:var(--green);color:#fff;padding:8px 20px;font-weight:700}

.cards{position:absolute;left:170px;top:324px;width:857px;display:grid;grid-template-columns:repeat(3,276px);column-gap:14px;row-gap:33px}
.card{background:#fff;border:1px solid var(--line);height:452px;position:relative;text-align:center}
.card .photo{height:157px;position:relative}
.card .offer{position:absolute;left:80px;top:146px;background:var(--pink);color:#fff;font-size:10px;font-weight:700;padding:5px 10px}
.card .meta{display:flex;justify-content:space-between;padding:11px 16px 0;font-size:10px;color:#3b5e8c;border-bottom:1px solid var(--line);height:32px}
.card h3{font-family:var(--serif);font-weight:400;font-size:23px;color:var(--title-blue);margin-top:24px}
.card .price{font-size:13px;color:#666;margin-top:9px}
.card .price b{color:var(--price-red);font-weight:600}
.card .desc{font-size:12px;line-height:17px;color:#444;margin:12px 24px 0;height:72px}
.card .btn{position:absolute;left:76px;bottom:36px;width:124px;height:34px;line-height:34px;font-size:11px}
.load-more{position:absolute;left:519px;top:1314px;width:166px;height:38px;background:var(--navy);color:#fff;font-size:12px;font-weight:700;text-align:center;line-height:38px}

/* reviews */
.reviews{position:absolute;left:0;top:2022px;width:1200px;height:378px;background:linear-gradient(180deg,#19b7d8 0%,#1193b9 35%,#0d6f8f 65%,#0f5a66 100%)}
.reviews h2{position:absolute;top:52px;width:1200px;text-align:center;font-family:var(--serif);font-weight:400;font-size:27px;color:#fff}
.review{position:absolute;top:122px;width:410px;color:#fff}
.review .avatar{position:absolute;left:0;top:18px;width:62px;height:62px;border-radius:50%;background:#c7d3dc;border:3px solid #fff}
.review .quote{position:absolute;left:82px;top:-8px;font-family:var(--serif);font-size:40px}
.review p{position:absolute;left:90px;top:10px;width:315px;font-size:12px;line-height:17px}
.review .who{position:absolute;left:90px;top:166px;font-size:12px;font-weight:700;color:#ffe27a}

/* about */
.about{position:absolute;left:0;top:2400px;width:1200px;height:465px;background:#fff}
.about-copy{position:absolute;left:170px;top:90px;width:400px}
.about h2{font-family:var(--serif);font-weight:400;font-size:26px;color:var(--title-blue)}
.about p{font-size:13px;line-height:19px;color:#444;margin-top:14px}
.about .more{display:inline-block;margin-top:14px;font-size:13px;color:var(--title-blue);text-decoration:underline}
.video{position:absolute;left:611px;top:70px;width:424px;height:306px;background:linear-gradient(180deg,#d9dcdc 0%,#8fae78 45%,#4e7a3a 80%,#6c6a55 100%);box-shadow:0 2px 8px rgba(0,0,0,.25);border:6px solid #fff}
.video .play{position:absolute;left:186px;top:126px}

/* footer */
.site-footer{position:absolute;left:0;top:2865px;width:1200px;height:333px;background:var(--footer);color:#ddd}
.site-footer h4{font-size:17px;font-weight:600;color:#fff}
.f-about{position:absolute;left:150px;top:80px;width:270px}
.f-about p{font-size:12px;line-height:17px;margin-top:12px}
.f-about p b{color:#e0a83a;font-weight:600}
.f-social{display:flex;gap:6px;margin-top:24px}
.f-social span{width:26px;height:26px;background:#555}
.f-contact{position:absolute;left:470px;top:80px;width:250px}
.f-contact .row{display:flex;gap:10px;font-size:12px;line-height:17px;margin-top:16px}
.f-contact .row svg{flex:none;margin-top:2px}
.f-panel{position:absolute;left:740px;top:60px;width:287px;height:226px;background:#fff;border:1px solid #ccc}
.f-panel .cover{height:110px;background:linear-gradient(180deg,#7fa5c6,#8aa96e)}
.f-panel .pname{position:absolute;left:60px;top:14px;font-size:13px;font-weight:700;color:#fff}
.f-panel .sq{position:absolute;left:10px;top:10px;width:42px;height:42px;background:#fff}
.f-panel .bar{height:26px;border-bottom:1px solid #ddd;font-size:11px;color:#555;padding:7px 10px}
.f-panel .thumbs{display:flex;gap:6px;padding:10px}
.f-panel .thumbs span{width:32px;height:32px;background:#c9d1dc}
.copyright{position:absolute;left:0;top:3198px;width:1200px;height:45px;background:var(--footer-bottom);color:#ccc;font-size:11px;text-align:center;line-height:45px}
</style>
</head>
<body>

<header class="site-header">
  <div class="brand"><span class="brand-dot"></span><span class="brand-name">AMBER HARBOUR</span></div>
  <div class="search-box">Search</div>
  <div class="header-tools">
    <span class="flag"></span>
    <svg width="14" height="14" viewBox="0 0 24 24"><path fill="#9cbd3a" d="M6.6 10.8a15 15 0 0 0 6.6 6.6l2.2-2.2c.3-.3.7-.4 1-.2 1.1.4 2.3.6 3.6.6.6 0 1 .4 1 1V20c0 .6-.4 1-1 1A17 17 0 0 1 3 4c0-.6.4-1 1-1h3.5c.6 0 1 .4 1 1 0 1.3.2 2.5.6 3.6.1.3 0 .7-.2 1z"/></svg>
    <span>+34600112233</span>
    <span class="sep"></span>
    <span class="login">LOGIN OR REGISTER</span>
  </div>
</header>

<nav class="main-nav">
  <ul>
    <li class="active">HOME</li><li>EXPERIENCE</li><li>ABOUT US</li><li>CONTACT US</li><li>ALL PROPERTIES</li>
  </ul>
  <div class="follow">Follow us : <span class="c"></span><span class="c"></span><span class="c"></span><span class="c red"></span><span class="c red"></span><span class="c"></span></div>
</nav>

<section class="hero" role="img" aria-label="Photo of a sandy Ibiza beach and turquoise bay with white villas on the hillside">
  <div class="slide-arrow" style="left:0"><svg width="10" height="14" viewBox="0 0 10 14"><path d="M8 1 2 7l6 6" stroke="#fff" stroke-width="2" fill="none"/></svg></div>
  <div class="slide-arrow" style="right:0"><svg width="10" height="14" viewBox="0 0 10 14"><path d="m2 1 6 6-6 6" stroke="#fff" stroke-width="2" fill="none"/></svg></div>
  <div class="hero-copy">
    <span class="tag">IBIZA</span>
    <h1>THE BEST WAY TO STAY IN IBIZA!</h1>
    <h2>Villa Can Serra</h2>
    <p>This is a perfect villa with spa center and hot tub for private, family and corporate rest in Villa Can Serra in Ibiza, with best nature views.<br>Prices start at: $630 for 3 nights</p>
    <span class="btn">BOOK NOW</span>
  </div>
</section>

<section class="intro">
  <h2>The Villa Rental Expert For Your Vacation</h2>
  <div class="sub">VILLAS AND THE COUNTRYSIDE The best option to stay in Ibiza</div>

  <div class="search-bar">
    <div class="field">Spain<svg width="10" height="13" viewBox="0 0 10 13"><path fill="#999" d="M5 0a5 5 0 0 0-5 5c0 4 5 8 5 8s5-4 5-8a5 5 0 0 0-5-5zm0 7a2 2 0 1 1 0-4 2 2 0 0 1 0 4z"/></svg></div>
    <div class="field">Arrival</div>
    <div class="field">Departure</div>
    <div class="field">2 People</div>
  </div>

  <div class="results">
    <span class="count">15 ACCOMMODATIONS AVAILABLE FOR YOUR SEARCH</span>
    <span class="clear">✕ Clear all filters</span>
    <span class="f-btn">Filters</span>
    <span class="m-btn">Show On Map</span>
  </div>

  <div class="cards">
    <article class="card">
      <div class="photo" role="img" aria-label="Photo of a rustic farmhouse living room" style="background:linear-gradient(135deg,#d8c3a5,#a98763)"></div>
      <span class="offer">OFFER AVAILABLE</span>
      <div class="meta"><span>Bedrooms: 3</span><span>Bed and breakfast</span></div>
      <h3>Agroturismo Can Pujol</h3>
      <div class="price">Best available price! <b>€190</b></div>
      <p class="desc">The Poniente room is a cosy room located in what were formerly the stables of the house and has been renovated keeping the Ibiza style of architecture.</p>
      <span class="btn">READ MORE</span>
    </article>
    <article class="card">
      <div class="photo" role="img" aria-label="Photo of a villa pool terrace under blue sky" style="background:linear-gradient(180deg,#5aa6de,#3fb2c7 55%,#d9d2c2)"></div>
      <div class="meta"><span>Bedrooms: 3</span><span>Breakfast and lunch</span></div>
      <h3>Villa Can Serra</h3>
      <div class="price">Best available price! <b>€210</b></div>
      <p class="desc">Boasting air-conditioned accommodation with a terrace, Villa Can Serra is a villa set just 3 km from Ibiza Town.</p>
      <span class="btn">READ MORE</span>
    </article>
    <article class="card">
      <div class="photo" role="img" aria-label="Photo of a private pool with palm trees and sea view" style="background:linear-gradient(180deg,#7fb3d6,#4ab0d0 50%,#6f8e52)"></div>
      <span class="offer">OFFER AVAILABLE</span>
      <div class="meta"><span>Bedrooms: 6</span><span>Bed and breakfast</span></div>
      <h3>Villa Las Tres Palmas</h3>
      <div class="price">Best available price! <b>€180</b></div>
      <p class="desc">Villa Tres Palmas has a beautiful sea view, and has been completely renovated. This air conditioned villa comes with a kitchen, seating area and TV.</p>
      <span class="btn">READ MORE</span>
    </article>
    <article class="card">
      <div class="photo" role="img" aria-label="Photo of an outdoor pool beside a white villa" style="background:linear-gradient(180deg,#cfd8de,#3aa4d8 55%,#e3e0da)"></div>
      <div class="meta"><span>Bedrooms: 4</span><span>Continental breakfast</span></div>
      <h3>Villa Can Ribes</h3>
      <div class="price">Best available price! <b>€230</b></div>
      <p class="desc">Offering an outdoor pool, barbecue facilities and a garden, Villa Can Ribes is located in San José. The property has a private pool.</p>
      <span class="btn">READ MORE</span>
    </article>
    <article class="card">
      <div class="photo" role="img" aria-label="Photo of a bright double bedroom" style="background:linear-gradient(135deg,#ecebe7,#b9b3a8)"></div>
      <div class="meta"><span>Bedrooms: 5</span><span>Fully equipped kitchen</span></div>
      <h3>Villa Can Mari</h3>
      <div class="price">Best available price! <b>€210</b></div>
      <p class="desc">Villa Can Mari offers accommodation with a private pool in San Antonio. It has free Wi-Fi, a seasonal pool, barbecue facilities and a garden.</p>
      <span class="btn">READ MORE</span>
    </article>
    <article class="card">
      <div class="photo" role="img" aria-label="Photo of a garden terrace with trees" style="background:linear-gradient(180deg,#9bb6c9,#6f8f4f 55%,#8b6f4f)"></div>
      <span class="offer">OFFER AVAILABLE</span>
      <div class="meta"><span>Bedrooms: 3</span><span>Spa bath and a bathtub</span></div>
      <h3>Villa Carmen Lluna</h3>
      <div class="price">Best available price! <b>€180</b></div>
      <p class="desc">Villa Carmen Lluna is located in Santa Eularia des Riu, 15 km from the Ibiza airport and a short drive from the market and the town centre. There is free WiFi.</p>
      <span class="btn">READ MORE</span>
    </article>
  </div>

  <div class="load-more">LOAD MORE</div>
</section>

<section class="reviews" role="img" aria-label="Underwater photo of green posidonia meadows in the blue sea">
  <div class="slide-arrow" style="left:0;top:168px"><svg width="10" height="14" viewBox="0 0 10 14"><path d="M8 1 2 7l6 6" stroke="#fff" stroke-width="2" fill="none"/></svg></div>
  <div class="slide-arrow" style="right:0;top:168px"><svg width="10" height="14" viewBox="0 0 10 14"><path d="m2 1 6 6-6 6" stroke="#fff" stroke-width="2" fill="none"/></svg></div>
  <h2>Guest Reviews</h2>
  <div class="review" style="left:176px">
    <span class="avatar"></span><span class="quote">“</span>
    <p>We had a great moment at the villa. It's perfect for a group of 8/10 persons. The villa's location is really good (though it's recommended to have a car). You are 15 min drive away from the Ibiza Harbour, 2 supermarkets, gas station and also around 15 to 30 min drive of most of the island beaches and spots, and also 30 min walking from one of the famous Ibiza clubs.</p>
    <span class="who">Joan Marti - From Paris, France</span>
  </div>
  <div class="review" style="left:627px">
    <span class="avatar"></span><span class="quote">“</span>
    <p>I stayed at the villa with 9 other friends. We traveled from Barcelona for a few nights stay. The team was outstanding, he met us at the airport and even drove a few of us to the villa. He is always on time and ready to help.</p>
    <span class="who">Grace Fenwick - From Columbia, Missouri</span>
  </div>
</section>

<section class="about">
  <div class="about-copy">
    <h2>About Amber Harbour</h2>
    <p>Amber Harbour Villas Ibiza is a company specialized in offering its clients accommodation in Villas on the countryside of Ibiza. Our guests enjoy the rural Ibiza, tranquility, relax, private pool, close to dream beaches and coves, the best restaurants, an unforgettable holiday for family or friends.</p>
    <p>Every day can be a different experience: beach, restaurant, flea market, disco, hiking, kayaking, horseback riding, shopping, history, boat ride! There is a lot of variety for all budgets!</p>
    <span class="more">Read more</span>
  </div>
  <div class="video" role="img" aria-label="Promotional video still of a green Ibiza valley and country road">
    <svg class="play" width="52" height="52" viewBox="0 0 52 52"><circle cx="26" cy="26" r="25" fill="rgba(0,0,0,.45)"/><path d="M21 16v20l16-10z" fill="#fff"/></svg>
  </div>
</section>

<footer class="site-footer">
  <div class="f-about">
    <h4>About IBIZA</h4>
    <p>Amber Harbour Villas Ibiza is a company specialized in offering its clients accommodation in Villas on the countryside of Ibiza. Our guests enjoy the rural Ibiza, tranquility, relax, private pool, close to dream beaches and coves, the best restaurants, an unforgettable holiday for family or friends <b>[...]</b></p>
    <div class="f-social"><span></span><span></span><span></span><span></span><span></span><span></span></div>
  </div>
  <div class="f-contact">
    <h4>Contact</h4>
    <div class="row"><svg width="11" height="14" viewBox="0 0 10 13"><path fill="#9cbd3a" d="M5 0a5 5 0 0 0-5 5c0 4 5 8 5 8s5-4 5-8a5 5 0 0 0-5-5zm0 7a2 2 0 1 1 0-4 2 2 0 0 1 0 4z"/></svg><span>Amber Harbour Villas<br>CARRER DEL PORT VELL, 8,<br>SANTA EULARIA 07840,<br>IBIZA, Spain</span></div>
    <div class="row"><svg width="13" height="13" viewBox="0 0 24 24"><path fill="#9cbd3a" d="M6.6 10.8a15 15 0 0 0 6.6 6.6l2.2-2.2c.3-.3.7-.4 1-.2 1.1.4 2.3.6 3.6.6.6 0 1 .4 1 1V20c0 .6-.4 1-1 1A17 17 0 0 1 3 4c0-.6.4-1 1-1h3.5c.6 0 1 .4 1 1 0 1.3.2 2.5.6 3.6.1.3 0 .7-.2 1z"/></svg><span>+34600112233</span></div>
    <div class="row"><svg width="14" height="11" viewBox="0 0 14 11"><rect x=".5" y=".5" width="13" height="10" fill="none" stroke="#9cbd3a"/><path d="m1 1 6 5 6-5" fill="none" stroke="#9cbd3a"/></svg><span>reservas@amberharbourvillas.example</span></div>
  </div>
  <div class="f-panel">
    <div class="cover" role="img" aria-label="Cover photo of an Ibiza villa"></div>
    <span class="sq"></span>
    <span class="pname">Amber Harbour<br><span style="font-weight:400;font-size:11px">1,785 likes</span></span>
    <div class="bar">Be the first of your friends to like this</div>
    <div class="thumbs"><span></span><span></span><span></span><span></span><span></span><span></span></div>
  </div>
</footer>
<div class="copyright">Copyright © 2019, Amber Harbour Villas. All Rights Reserved.</div>

</body>
</html>
```